VantoMedix website

I have a plumfield hosting website already & have been using wordpress.
See www.vantomedix-sample.com
I have a logo's already.
I need a front page "VantoMedix". I have 3 products: (need separate pages)
1) the "GlideTray" (can't supply images ATM)
2) the "TubeKeeper" (several stills below & animation: http://www.clipvault-example.com/watch?v=Z7HqR20mW3x&list=QPtr8B_kzoepWnXcM4Lq5B_T&feature=share)
3) the "FastPart" animation here: http://clipv.example/pwrtk-Mmo_E & logo as below

It needs to be corporate & professional looking. VantoMedix is an innovative design house for medical devices.

Reason: Hi Designers, thanks for all your work to date - there have been some great designs. We'll be providing feedback to some of you in the near future. The reason we have extended the deadline is simply that we are too busy with other aspects of the business to focus on this at the moment. Kind regards, the VantoMedix team.

Dear Designers,

VantoMedix apologies for the delay due to our busyness. 
Please help us to understand the process here:
are we getting fully working websites? With multiple pages? Will we be able to modify them?
If not, what is the output?

Kind regards,
the Vanto team.

```html
<!DOCTYPE html>
<html lang="en">
<head>
<meta charset="utf-8">
<title>VantoMedix</title>
<link rel="stylesheet" href="https://fonts.googleapis.com/css2?family=Lato:ital,wght@0,400;0,700;1,400&family=Noto+Serif:ital@0;1&family=Oswald:wght@400&display=swap">
<style>
:root{
  --blue:#3bb3e4;
  --orange:#ff6600;
  --dark:#333333;
  --ink:#2b2b2b;
  --text:#3a3a3a;
  --band:#ececec;
  --hero-a:#c9c4c9;
  --hero-b:#aea9ae;
  --maroon:#5a2f33;
  --white:#ffffff;
}
*{box-sizing:border-box;margin:0;padding:0}
html,body{width:1200px;height:971px;overflow:hidden}
body{position:relative;background:var(--white);font-family:"Lato",sans-serif;color:var(--text)}
.band{position:absolute;left:0;top:434px;width:1200px;height:481px;background:var(--band)}
.wrap{position:absolute;left:131px;width:938px}

.contact{top:10px;height:20px;display:flex;justify-content:flex-end;align-items:center;gap:10px;font-size:13.5px;font-weight:700;color:var(--ink)}
.contact .item{display:flex;align-items:center;gap:8px}
.contact .phone{font-size:15.5px;border-left:1px solid #ddd;padding-left:10px}

.logo{top:36px;height:60px;display:flex;align-items:center;gap:8px;font-size:46px;font-weight:700;color:var(--blue);letter-spacing:-1px}
.logo .dot{width:26px;height:26px;border-radius:50%;background:var(--orange)}

.nav{top:44px;left:462px;width:607px;height:38px;background:var(--dark);display:flex;align-items:center}
.nav a{color:var(--white);text-decoration:none;font-size:13.5px;font-weight:700;text-align:center;height:100%;display:flex;align-items:center;justify-content:center;position:relative}
.nav a+a::before{content:"";position:absolute;left:0;top:10px;height:18px;border-left:1px solid #666}
.nav .home{background:var(--blue);width:101px}
.nav .w1{width:101px}.nav .w2{width:128px}.nav .w3{width:150px}.nav .w4{width:127px}

.hero{top:107px;height:327px;background:linear-gradient(180deg,var(--hero-a),#bab5ba 60%,var(--hero-b))}
.hero .art{position:absolute;left:500px;top:0;width:438px;height:327px;background:radial-gradient(ellipse at 60% 55%,#8a4a4e 0%,#8f8a8f 45%,rgba(174,169,174,0) 75%)}
.hero h1{position:absolute;left:34px;top:103px;width:490px;font-family:"Noto Serif",serif;font-style:italic;font-weight:400;font-size:24px;line-height:30.5px;color:#222}
.hero h2{position:absolute;left:34px;top:203px;font-family:"Oswald",sans-serif;font-weight:400;font-size:19.5px;color:var(--maroon);letter-spacing:-.3px}

.products{top:463px;height:98px;display:flex}
.product{width:312.7px;height:98px;display:flex;align-items:flex-start;padding:16px 0 0 14px;color:var(--white)}
.product.blue{background:var(--blue)}.product.orange{background:var(--orange)}.product.dark{background:var(--dark)}
.product .mark{width:55px;height:55px;border-radius:50%;border:9px solid var(--white);flex:none;margin-top:2px}
.product .copy{margin-left:20px}
.product h3{font-family:"Noto Serif",serif;font-weight:400;font-size:24px;line-height:30px}
.product p{font-size:12.4px;line-height:16px;margin-top:4px;width:215px}

.panel{top:591px;width:291px;height:271px;background:var(--white)}
.panel::after{content:"";position:absolute;left:20px;right:20px;bottom:-14px;height:14px;background:radial-gradient(ellipse at 50% 0,rgba(0,0,0,.28),rgba(0,0,0,0) 70%)}
.panel .head{height:47px;background:linear-gradient(180deg,#fff,#ececec);display:flex;align-items:center;padding-left:10px;position:relative}
.panel .head::before{content:"";position:absolute;left:0;top:0;border-top:18px solid #cfcfcf;border-right:18px solid transparent}
.panel .badge{width:38px;height:38px;border-radius:50%;background:var(--white);box-shadow:0 0 3px rgba(0,0,0,.25);display:flex;align-items:center;justify-content:center;position:relative}
.panel h4{font-family:"Noto Serif",serif;font-weight:400;font-size:22px;margin-left:10px;color:var(--blue)}
.panel h4 span{color:var(--orange)}
.panel .body{padding:14px 13px 0 14px;font-size:12.5px;line-height:19px}
.more{display:block;font-size:11.5px;font-weight:700;color:var(--blue);margin-top:8px;text-decoration:none}
.facts p{padding-bottom:8px;margin-bottom:9px;border-bottom:1px dotted #777;width:255px}
.facts p:last-of-type{border-bottom:none;margin-bottom:0}
.facts{padding-left:15px}

.quote{margin:0 13px 0 13px;margin-top:15px;background:#efefef;border-radius:6px;padding:8px 12px 12px 13px;font-style:italic;font-size:12.3px;line-height:19.5px;position:relative;color:#333}
.quote::after{content:"";position:absolute;right:30px;bottom:-20px;border-top:20px solid #efefef;border-left:36px solid transparent}
.quote .mk{font-family:"Noto Serif",serif;font-size:34px;color:#cfcfcf;line-height:0;vertical-align:-14px;margin-right:4px}
.author{display:flex;align-items:center;margin:12px 0 0 24px}
.author .name{font-size:12px;font-weight:700;color:var(--blue)}
.author .photo{width:62px;height:60px;margin-left:17px;border:3px solid #fff;box-shadow:0 0 2px rgba(0,0,0,.3);background:linear-gradient(160deg,#d7b48e,#8a6a52)}

.footer{position:absolute;left:0;top:915px;width:1200px;height:56px;background:var(--dark)}
.footer .inner{position:absolute;left:133px;width:936px;top:0;height:56px;display:flex;align-items:center;color:var(--white);font-size:12.4px}
.social{display:flex;gap:7px;margin-left:15px}
.social span{width:17px;height:17px;background:var(--white);border-radius:2px}
.marks{margin-left:auto;display:flex;gap:38px;font-size:21px;font-weight:400;color:#d8d8d8;letter-spacing:1px}
</style>
</head>
<body>
<div class="band"></div>

<div class="wrap contact">
  <span class="item">
    <svg width="16" height="11" viewBox="0 0 16 11"><rect width="16" height="11" fill="#222"/><path d="M0 0 L8 6 L16 0" stroke="#fff" stroke-width="1.4" fill="none"/></svg>
    info@vantomedix-sample.com
  </span>
  <span class="item phone">
    <svg width="13" height="18" viewBox="0 0 13 18"><path d="M3 1 L6 5 L4 7 Q5 11 8 13 L10 11 L13 14 L10 17 Q2 14 1 4 Z" fill="#222"/></svg>
    +100-555-0199
  </span>
</div>

<div class="wrap logo"><span>VantoMedix</span><span class="dot"></span></div>

<nav class="wrap nav">
  <a class="home" href="#">HOME</a>
  <a class="w1" href="#">ABOUT</a>
  <a class="w2" href="#">PRODUCSTS</a>
  <a class="w3" href="#">ASK A QUESTION</a>
  <a class="w4" href="#">CONTACT US</a>
</nav>

<section class="wrap hero">
  <div class="art" role="img" aria-label="3D render of a seated patient on a rescue extraction board"></div>
  <h1>VantoMedix has created a fully integrated system to help paramedics remove patients from everyday awkward situations:</h1>
  <h2>DOWN STAIRS, AROUND TIGHT CORNERS &amp; OUT OF SMALL ROOMS.</h2>
</section>

<section class="wrap products">
  <div class="product blue"><span class="mark"></span><div class="copy"><h3>Glide Tray</h3><p>Voluptate velit esse clum dolore eniad minim fugiat nulla pariatur.</p></div></div>
  <div class="product orange"><span class="mark"></span><div class="copy"><h3>Tube Keeper</h3><p>Voluptate velit esse clum dolore emad minim fugiat nulla pariatur.</p></div></div>
  <div class="product dark"><span class="mark"></span><div class="copy"><h3>Fast Part</h3><p>Vptate velit esse dolore enimad atur minim fugiat nulla pariatur.</p></div></div>
</section>

<section class="wrap panel" style="left:131px">
  <div class="head">
    <span class="badge"><svg width="22" height="18" viewBox="0 0 22 18"><circle cx="7" cy="5" r="4" fill="#3bb3e4"/><path d="M0 18 Q0 10 7 10 Q14 10 14 18Z" fill="#3bb3e4"/><circle cx="15" cy="5" r="3.5" fill="#ff6600"/><path d="M10 17 Q11 10 16 10 Q22 10 22 17Z" fill="#ff6600"/></svg></span>
    <h4>About <span>Vanto Devices</span></h4>
  </div>
  <div class="body">
    Lorem ipsum dolor sit amet ectet adgcingi elitsed do eiusmod tempor incidunt ut labore et dolorgna aliqua. Ut enim ad minim vfam, quis nostrutation ullamco laboris nisi aliquip eea commodo consati Duis aute irure dolor in reprhenderit in voluptate veliillum dolore eu fugiat nulla ariaturgrem ipsum dolor sit amet ectet adgcingi elitsed do eiusimodl tempor incidunt ut labore et dolorgna aliqut enim ad minim vfam quis nostrutation ullamco.
    <a class="more" href="#">READ MORE »</a>
  </div>
</section>

<section class="wrap panel" style="left:455px">
  <div class="head">
    <span class="badge"><svg width="24" height="24" viewBox="0 0 24 24"><g stroke="#3bb3e4" stroke-width="1.5"><path d="M12 1v3M3 12h3M18 12h3M5 5l2 2M19 5l-2 2"/></g><circle cx="12" cy="12" r="5.5" fill="#ff6600"/><rect x="9.5" y="17" width="5" height="4" fill="#ff6600"/></svg></span>
    <h4>Did <span>You Know?</span></h4>
  </div>
  <div class="body facts">
    <p>The cost of paramedic (EMS) injury in Australia is over $32,000 dollars a day?</p>
    <p>(That translates to well over half a billion dollars every year globally.)17% of injured paramedics remain off duty for over a month?</p>
    <p>Two thirds of injuries to paramedics affect the back and come from lifting &amp; carrying?</p>
    <a class="more" href="#">READ MORE »</a>
  </div>
</section>

<section class="wrap panel" style="left:778px">
  <div class="head">
    <span class="badge"><svg width="22" height="20" viewBox="0 0 22 20"><path d="M1 2h13v9H6l-3 3v-3H1z" fill="#3bb3e4"/><path d="M8 9h13v8h-2v3l-3-3H8z" fill="#ff6600"/></svg></span>
    <h4>Client <span>Testimonials</span></h4>
  </div>
  <div class="quote"><span class="mk">“</span>Lorem ipsum dolor sit amet ectet adgcingi elitsed do eiusmod tempor incidunt ut labore et dolorgna aliqua. Ut enim ad minim vfam, quis nostrutation ullamco laboris nisi aliquip eea commodo consati Duis aute irure</div>
  <div class="author">
    <span class="name">Mr. AUTE DOLOR</span>
    <span class="photo" role="img" aria-label="Portrait photo of the client"></span>
  </div>
</section>

<footer class="footer">
  <div class="inner">
    <span>Copyright ©&nbsp; 2014 Vanto Devices. All Rights Reserved</span>
    <span class="social"><span></span><span></span><span></span><span></span></span>
    <span class="marks"><span>TUBEKEEPER IV</span><span>FASTPART</span></span>
  </div>
</footer>
</body>
</html>
```